Need a professional card design. Marlowe building company specialise in residential and commercial builds. New homes, additions & renovations.
Wanting a card with creativity and professionalism.
Want card that utilises logo.

Back and front.

I have just created a logo, and want to use it on the business card.
Attached a copy of the logo.
Attached is also a current business card which I wish to redesign

please utilise both sides

• Reg# 38095

```html
<!DOCTYPE html>
<html lang="en">
<head>
<meta charset="utf-8">
<title>Marlowe Building Co – Business Card</title>
<link rel="stylesheet" href="https://fonts.googleapis.com/css2?family=Oswald:wght@500;600&family=Open+Sans:wght@400&family=Roboto+Condensed:wght@400&display=swap">
<style>
  :root {
    --page-bg: #f1f1f1;
    --card-dark: #231f20;
    --card-light: #ffffff;
    --accent: #f0a02c;
    --ink: #1e1e1e;
    --icon-grey: #8a8a8a;
    --rule: #2a2a2a;
    --white: #ffffff;
  }
  * { margin: 0; padding: 0; box-sizing: border-box; }
  html, body {
    width: 1200px; height: 900px; overflow: hidden;
    background: var(--page-bg);
  }
  .canvas {
    position: relative; width: 1200px; height: 900px;
  }
  .card {
    position: absolute; top: 290px;
    width: 560px; height: 320px;
    box-shadow: 3px 4px 10px rgba(0,0,0,0.35);
  }
  /* Front */
  .card-front { left: 30px; background: var(--card-dark); }
  .front-brand {
    position: absolute; top: 92px; left: 0; width: 100%;
    display: flex; justify-content: center; align-items: center; gap: 14px;
    font-family: "Open Sans", sans-serif; font-weight: 400;
    font-size: 40px; color: var(--accent); letter-spacing: 1px;
  }
  .brand-dot {
    width: 18px; height: 18px; border-radius: 50%; background: var(--accent);
  }
  .front-services {
    position: absolute; top: 222px; left: 0; width: 100%;
    text-align: center; color: var(--white);
    font-family: "Open Sans", sans-serif; font-size: 22px; line-height: 30px;
  }
  .service-dot { color: var(--accent); }

  /* Back */
  .card-back { left: 610px; background: var(--card-light); }
  .holder-name {
    position: absolute; top: 22px; left: 26px;
    font-family: "Oswald", sans-serif; font-weight: 600;
    font-size: 32px; line-height: 36px; letter-spacing: 0.5px; color: var(--ink);
  }
  .holder-name .surname { color: var(--accent); }
  .holder-role {
    position: absolute; top: 60px; left: 27px;
    font-family: "Roboto Condensed", sans-serif; font-size: 13px;
    letter-spacing: 4px; color: var(--accent);
  }
  .rule {
    position: absolute; left: 26px; width: 222px; height: 2px; background: var(--rule);
  }
  .rule-top { top: 98px; }
  .rule-bottom { top: 252px; }
  .contact-list { position: absolute; top: 108px; left: 26px; list-style: none; }
  .contact-list li {
    display: flex; align-items: center; height: 35px;
    font-family: "Roboto Condensed", sans-serif; font-size: 14px; color: var(--ink);
  }
  .contact-icon { width: 30px; height: 24px; margin-right: 12px; flex: none; }
  .address {
    position: absolute; top: 260px; left: 26px;
    font-family: "Roboto Condensed", sans-serif; font-size: 16px; color: var(--ink);
  }
  .back-brand {
    position: absolute; top: 238px; right: 24px;
    display: flex; align-items: center; gap: 7px;
    font-family: "Open Sans", sans-serif; font-weight: 400;
    font-size: 18px; color: var(--accent);
  }
  .back-brand .brand-dot { width: 9px; height: 9px; }
</style>
</head>
<body>
<main class="canvas">

  <section class="card card-front" aria-label="Card front">
    <div class="front-brand"><span class="brand-dot"></span><span>Marlowe Building Co</span></div>
    <p class="front-services">
      New Homes<span class="service-dot">•</span>Additions &amp; Renovations<br>
      Domestic &amp; Commercial Builders
    </p>
  </section>

  <section class="card card-back" aria-label="Card back">
    <h1 class="holder-name">DANIEL <span class="surname">HARROW</span></h1>
    <p class="holder-role">DIRECTOR</p>
    <div class="rule rule-top"></div>
    <ul class="contact-list">
      <li>
        <svg class="contact-icon" viewBox="0 0 30 24" aria-hidden="true">
          <path d="M3 9 Q15 1 27 9 L24 12 L20 9 L10 9 L6 12 Z" fill="none" stroke="var(--icon-grey)" stroke-width="1.6"/>
          <rect x="7" y="12" width="16" height="9" rx="2" fill="none" stroke="var(--icon-grey)" stroke-width="1.6"/>
          <circle cx="15" cy="16.5" r="2.4" fill="none" stroke="var(--icon-grey)" stroke-width="1.4"/>
        </svg>
        08 9412 6650
      </li>
      <li>
        <svg class="contact-icon" viewBox="0 0 30 24" aria-hidden="true">
          <rect x="8" y="2" width="14" height="8" fill="var(--icon-grey)"/>
          <rect x="3" y="10" width="24" height="10" rx="2" fill="var(--icon-grey)"/>
          <rect x="8" y="16" width="14" height="6" fill="#ffffff" stroke="var(--icon-grey)" stroke-width="1.4"/>
        </svg>
        08 9412 6650
      </li>
      <li>
        <svg class="contact-icon" viewBox="0 0 30 24" aria-hidden="true">
          <rect x="8" y="1" width="14" height="22" fill="none" stroke="var(--icon-grey)" stroke-width="1.4"/>
          <text x="15" y="16" text-anchor="middle" font-family="Roboto Condensed, sans-serif" font-size="10" fill="var(--icon-grey)">M</text>
        </svg>
        0412 555 019
      </li>
      <li>
        <svg class="contact-icon" viewBox="0 0 30 24" aria-hidden="true">
          <rect x="2" y="4" width="26" height="16" fill="none" stroke="var(--icon-grey)" stroke-width="1.6"/>
          <path d="M2 4 L15 14 L28 4 M2 20 L11 11 M28 20 L19 11" fill="none" stroke="var(--icon-grey)" stroke-width="1.4"/>
        </svg>
        MARLOWEBUILDINGCO@MAILBOX.COM
      </li>
    </ul>
    <div class="rule rule-bottom"></div>
    <p class="address">24 Harbour Lane&nbsp; Kinross WA 6031</p>
    <div class="back-brand"><span class="brand-dot"></span><span>Marlowe Building Co</span></div>
  </section>

</main>
</body>
</html>
```